LABEL DESIGNS FOR SKINCARE LINE

Hello we are needing 12 label various label designs but would like to see you design ONE. We will pick winner from this and send the rest.
LABEL SIZE -2x7
JAR SIZE IS - 8oz
LOGOS FILES BELOW
https://files.pavorna-share.net/drive/folders/7xk3q-wumTrazPLoqVnnRTZBKHAE2DpLW
INFORMATION FOR LABEL
Calm Dune Hush Whipped Body Sugar Scrub 8oz
Ideal for all Skin Types
Ingredients:
Pure Cane Sugar, Extra Virgin Coconut Oil, Mango Butter, Kukum Butter, Emulsifying Wax, Jojoba Seed Oil, Sweet Almond Oil, Strawberry Essential Oil, and Pomegranate Essential Oil.
Directions to use Body Sugar Scrub:
Apply to wet skin gently in a circular motion on desired body area, hands, feet, legs, arms, etc. Once you have a good scrub, rinse, pat dry, and enjoy soft, hydrated skin. Best to use in the shower. Use between 2-3 times a week if needed.
*Cautions:
(1) Allergy: Approach this product with extreme caution, if you have allergies
(2) Avoid direct contact with eyes
Storage/Shelf Life of Product:
For best results, stir/mix scrub with the wooden or plastic spoon before each use. The shelf life of all sugar scrubs is 6-8 weeks. Keep the product in a cool, dry place, away from hot or heated temperatures.
All Natural, Cruelty-Free, Vegan Free
No Mineral Oil
No Petroleum
No Parabens

```html
<!DOCTYPE html>
<html lang="en">
<head>
<meta charset="utf-8">
<title>Calm Dune Hush Whipped Body Sugar Scrub Label</title>
<link href="https://fonts.googleapis.com/css2?family=Nunito:wght@400;600;700;800&display=swap" rel="stylesheet">
<style>
  :root {
    --backdrop: #e6e4e5;
    --label-white: #ffffff;
    --sage: #a9c48a;
    --sage-deep: #8fae6e;
    --leaf-warm: #d9b07a;
    --ink: #1f2a1c;
    --panel-text: #ffffff;
    --pink: #e89bb4;
    --pink-soft: #efa9c0;
    --teal: #3fb7a8;
    --icon-green: #6aa84f;
  }
  * { box-sizing: border-box; margin: 0; padding: 0; }
  html, body { width: 1200px; height: 1000px; overflow: hidden; }
  body {
    background: var(--backdrop);
    font-family: "Nunito", Arial, sans-serif;
    position: relative;
  }
  .label {
    position: absolute;
    left: 63px; top: 348px;
    width: 1074px; height: 303px;
    background: var(--label-white);
    box-shadow: 0 6px 18px rgba(0,0,0,.12);
  }
  .panel {
    position: absolute;
    top: 17px; height: 273px;
    background: var(--sage);
    overflow: hidden;
  }
  .panel--info { left: 0; width: 314px; padding: 28px 22px 0 22px; color: var(--ink); }
  .panel--care { left: 720px; width: 354px; padding: 38px 18px 0 18px; color: var(--panel-text); }
  .foliage {
    position: absolute;
    pointer-events: none;
  }
  .foliage--info {
    left: 0; bottom: 0; width: 120px; height: 150px;
    background: radial-gradient(ellipse at 20% 90%, rgba(217,176,122,.55), rgba(169,196,138,0) 70%);
  }
  .foliage--care {
    right: 0; top: 0; width: 230px; height: 273px;
    background: radial-gradient(ellipse at 75% 40%, rgba(217,176,122,.45), rgba(143,174,110,.35) 45%, rgba(169,196,138,0) 75%);
  }
  .panel h3 {
    font-size: 12px; font-weight: 700; letter-spacing: .3px;
    text-transform: uppercase; margin-bottom: 2px; position: relative;
  }
  .panel--info h3 { color: var(--panel-text); }
  .panel p { font-size: 10.5px; line-height: 1.38; position: relative; }
  .panel--info p + h3 { margin-top: 12px; }
  .panel--care h3 { text-transform: none; font-weight: 600; font-size: 11.5px; }
  .panel--care p { font-size: 11.5px; line-height: 1.32; }
  .panel--care .storage { margin-top: 26px; }
  .panel--care strong { color: var(--ink); font-weight: 700; }

  .front {
    position: absolute; left: 314px; width: 406px; top: 0; height: 303px;
    text-align: center;
  }
  .brand {
    margin-top: 48px;
    font-size: 38px; font-weight: 800; color: var(--pink);
    letter-spacing: .5px; line-height: 1;
  }
  .product {
    margin-top: 36px;
    font-size: 11.5px; font-weight: 600; color: var(--pink-soft); line-height: 1.3;
  }
  .claims {
    display: flex; justify-content: center; gap: 26px; margin-top: 10px;
  }
  .claim { width: 62px; font-size: 7px; font-weight: 600; color: var(--icon-green); }
  .claim svg { display: block; margin: 0 auto 4px; }
  .badge {
    margin-top: 24px; display: flex; justify-content: center; align-items: center; gap: 8px;
    font-size: 17px; font-weight: 600; color: var(--teal);
  }
  .size { font-size: 12px; color: var(--pink-soft); font-weight: 600; margin-top: 2px; }
</style>
</head>
<body>
  <main class="label">
    <section class="panel panel--info">
      <div class="foliage foliage--info" role="img" aria-label="Soft tropical leaf illustration"></div>
      <h3>Ingredients:</h3>
      <p>pure cane sugar, extra virgin coconut oil, mango butter, kukum butter, emulsifying wax, jojoba seed oil, sweet almond oil, strawberry essential oil, and pomegranate essential oil.</p>
      <h3>Directions to use body sugar scrub:</h3>
      <p>Apply to wet skin gently<br>in a circular motion on<br>desired body area,hands, feet, legs, arms, etc.<br>Once you have a good scrub, rinse,pat dry,<br>and enjoy soft, hydrated skin.<br>Best to use in the shower.<br>Use between 2-3 times a week if<br>needed.</p>
    </section>

    <section class="front">
      <div class="brand">Petal Hollow</div>
      <div class="product">Calm Dune Hush Whipped Body Sugar Scrub<br>Ideal for ALL SKIN TYPES</div>
      <div class="claims">
        <div class="claim">
          <svg width="30" height="30" viewBox="0 0 30 30" fill="none" stroke="var(--icon-green)" stroke-width="1.4">
            <path d="M17 6c-4 6-7 9-7 13a7 7 0 0 0 14 0c0-4-3-7-7-13z"/>
            <path d="M8 3c-1.5 2.5-3 3.5-3 5a3 3 0 0 0 6 0c0-1.5-1.5-2.5-3-5z"/>
            <circle cx="14" cy="20" r="1.5"/>
          </svg>No Mineral Oil</div>
        <div class="claim">
          <svg width="30" height="30" viewBox="0 0 30 30" fill="none" stroke="var(--icon-green)" stroke-width="1.4">
            <rect x="4" y="4" width="22" height="22" rx="3"/>
            <path d="M8 16h14l-2 6h-10z"/>
            <path d="M15 16c0-5 3-7 6-8-1 4-3 6-6 8zM15 16c-1-3-3-5-6-5 0 3 2 5 6 5z"/>
          </svg>Vegan Free</div>
        <div class="claim">
          <svg width="30" height="30" viewBox="0 0 30 30" fill="none" stroke="var(--icon-green)" stroke-width="1.4">
            <path d="M12 4h6M13 4v7a9 9 0 1 0 4 0V4"/>
            <path d="M8 19c3-2 5 1 7 0s4-2 7 0"/>
            <circle cx="13" cy="22" r="1"/><circle cx="18" cy="24" r="1"/>
          </svg>No Parabens</div>
        <div class="claim">
          <svg width="30" height="30" viewBox="0 0 30 30" fill="none" stroke="var(--icon-green)" stroke-width="1.4">
            <path d="M15 20c0-6 4-10 9-11-1 6-4 10-9 11zM15 20c-5-1-8-5-9-10 5 1 9 5 9 10z"/>
            <path d="M15 20v-9"/>
            <path d="M6 22h18l-2 4h-14z"/>
          </svg>No Petroleum</div>
      </div>
      <div class="badge">
        <svg width="22" height="20" viewBox="0 0 22 20" fill="var(--teal)">
          <path d="M11 10C11 5 8 2 5 1c-1 5 1 8 6 9zM11 10c0-5 3-8 6-9 1 5-1 8-6 9zM11 10c-4 0-8 2-9 6 4 1 8 0 9-6zM11 10c4 0 8 2 9 6-4 1-8 0-9-6z"/>
        </svg>
        All Natural Cruelty-Free
      </div>
      <div class="size">8oz</div>
    </section>

    <section class="panel panel--care">
      <div class="foliage foliage--care" role="img" aria-label="Soft palm leaf illustration"></div>
      <h3>*CAUTIONS:</h3>
      <p>(1) Allergy: Approach this product<br>&nbsp;with extreme caution, if you have allergies<br>(2) Avoid direct contact with eyes</p>
      <h3 class="storage">Storage/Shelf Life of Product:</h3>
      <p>For best results, stir/mix scrub<br>with the wooden or plastic spoon<br>before each use.<br>The shelf life of all sugar scrubs<br>is <strong>6-8 weeks</strong>. Keep the product<br>in a cool, dry place, away<br>from hot or heated temperatures.</p>
    </section>
  </main>
</body>
</html>
```